Company Poster - Balsent Merchant Group

Hello!

We are looking for a Company poster of the size:
Width - 1,800mm
Height - 1,635mm

This poster is the first thing that a visitor would see when he/she walks into our showroom.

Following are the data that needs to be understood:

Company Name
[BALSENT MERCHANT GROUP LLC]

Related Company logos that should be included in the poster:
[TUBRAVEX CANADA] [nature - Plastic piping systems]
[KARTUVEL] [nature - e-commerce site]
[BRISKET WORKSHOPS] [nature - web based software solutions]
[VELLUMORE CRAFT STUDIO] [nature - promoting artists]
[BLUE QUINCE - HONG KONG & MACAU] [nature - frozen yogurt]

The following files are attached in png and AI (where possible):

1] Balsent Merchant Group Theme and logo (multiple files)
2] Related Companies Logo (multiple files)
3] Pictures of the Physical location (multiple files)
4] Few poster sample (multiple files)

Please note that we usually like minimal designs. A simple idea would be to place the Balsent Logo and name in the centre and the related company logos at the bottom. However, we are very keen to see if we can get some creative design and not just minimal work.

If you need any further input, please let me know

regards
Tarun
Updates

Project Deadline Extended
Reason: It's quite surprising. For the first time, I haven't found a single design that is suitable. I am hoping I get a good design by the end of this extension thanks Tarun

Target Market(s)

Visitors who walk into the showroom

Industry/Entity Type

E-Commerce

Requirements
Must have
• Theme of the poster should be similar to the attached theme of BALSENT MERCHANT GROUP
Should not have
• Please don't make it too crowded. Minimal but creative.

```html
<!DOCTYPE html>
<html lang="en">
<head>
<meta charset="utf-8">
<title>Balsent Merchant Group – Showroom Poster</title>
<link rel="stylesheet" href="https://fonts.googleapis.com/css2?family=Questrial&family=Roboto+Slab:wght@800&display=swap">
<style>
  :root {
    --page-bg: #e9eaec;
    --poster-top: #0c1a2c;
    --poster-mid: #0a1f3a;
    --poster-edge: #050b14;
    --footer-bg: #040608;
    --title-blue: #1ea3e4;
    --mark-blue: #2f6fc0;
    --band-pipes: #1b9fdc;
    --band-fittings: #2173b8;
    --band-valves: #1c9a88;
    --band-accessories: #12736a;
    --band-text: #ffffff;
    --partner-text: #9ea4ab;
  }
  * { margin: 0; padding: 0; box-sizing: border-box; }
  html, body {
    width: 1200px;
    height: 800px;
    overflow: hidden;
    background: var(--page-bg);
  }
  .poster {
    position: absolute;
    left: 390px;
    top: 40px;
    width: 420px;
    height: 720px;
    overflow: hidden;
    background:
      radial-gradient(ellipse 70% 55% at 50% 35%, var(--poster-mid), var(--poster-top) 60%, var(--poster-edge) 100%);
    box-shadow: 0 6px 24px rgba(0, 0, 0, 0.18);
  }
  .brand {
    position: absolute;
    top: 112px;
    left: 0;
    width: 100%;
    text-align: center;
  }
  .brand-mark {
    display: block;
    width: 84px;
    height: 84px;
    margin: 0 auto 26px;
    background: var(--mark-blue);
    border-radius: 18px;
  }
  .brand-name {
    font-family: "Questrial", sans-serif;
    font-weight: 400;
    font-size: 24px;
    letter-spacing: 0.5px;
    color: var(--title-blue);
  }
  .range {
    list-style: none;
  }
  .range-band {
    position: absolute;
    right: 0;
    height: 26px;
    padding-left: 22px;
    display: flex;
    align-items: center;
    font-family: "Roboto Slab", serif;
    font-weight: 800;
    font-size: 14px;
    letter-spacing: 1px;
    text-transform: uppercase;
    color: var(--band-text);
    clip-path: polygon(8px 0, 100% 0, 100% 100%, 0 100%);
  }
  .range-band--pipes { top: 428px; left: 28px; background: var(--band-pipes); }
  .range-band--fittings { top: 464px; left: 62px; background: var(--band-fittings); }
  .range-band--valves { top: 500px; left: 122px; background: var(--band-valves); }
  .range-band--accessories { top: 536px; left: 176px; height: 30px; background: var(--band-accessories); font-size: 15px; }
  .partners {
    position: absolute;
    left: 0;
    bottom: 0;
    width: 100%;
    height: 120px;
    background: var(--footer-bg);
    display: flex;
    justify-content: space-between;
    align-items: flex-start;
    padding: 28px 18px 0;
    list-style: none;
  }
  .partner {
    font-family: "Questrial", sans-serif;
    font-weight: 400;
    font-size: 7.5px;
    letter-spacing: 0.3px;
    color: var(--partner-text);
    text-transform: uppercase;
    line-height: 1.2;
    display: flex;
    align-items: center;
    gap: 4px;
  }
  .partner-dot {
    width: 7px;
    height: 7px;
    border-radius: 50%;
    background: var(--partner-text);
    flex: none;
  }
</style>
</head>
<body>
  <main class="poster">
    <header class="brand">
      <span class="brand-mark" aria-hidden="true"></span>
      <h1 class="brand-name">BALSENT MERCHANT GROUP</h1>
    </header>

    <ul class="range">
      <li class="range-band range-band--pipes">Pipes</li>
      <li class="range-band range-band--fittings">Fittings</li>
      <li class="range-band range-band--valves">Valves</li>
      <li class="range-band range-band--accessories">Accessories</li>
    </ul>

    <ul class="partners">
      <li class="partner"><span class="partner-dot"></span>Tubravex<br>Canada</li>
      <li class="partner">Kartuvel</li>
      <li class="partner">Brisket<br>Workshops</li>
      <li class="partner">Vellumore<br>Craft Studio</li>
      <li class="partner"><span class="partner-dot"></span>Blue Quince</li>
    </ul>
  </main>
</body>
</html>
```